House-share and Room Rental Website (With Focus on the Bedroom Landing Page)

Looking for website design for our House-share (executive accommodation) and room rental business.

Our company name is: Lodvenra could also be written as LodVenra or lodvenra. Either is fine .. just looking for a nice clean catchy logo to go with the design.

EXAMPLES
These are examples of other websites in this field that are doing well. this is a kind of baseline.
https://kelbrin.com.au/
https://www.tuvaplex.com/
https://www.nestorvi.com/
https://www.quillsa.net/
https://www.pendlebarrow.com.au/

Our business model is to rent rooms to people looking for high-quality accommodation. We fill the gap between those looking to rent rooms and those with rooms to rent. However, our model is slightly different from those already on the market as we looking to fill a massive gap in the market delivering upmarket rooms for rent.(Executive Accommodation) also in the back end will be coupled with a self management process in the back end.

We offer executive style accommodation that stands out above the rest. With special extras like fire safety.. and management processes that create happier homes. We are looking for a web design package that can help us grow and scale our business. We need a design that is captivating

Our MAIN focus is having a room landing page that stands out from the rest... The core of our business will rely on the promotion of the rooms in a share house... so the whole design relies on the BEDROOM landing page to drive results.

Target Market(s)

We have 2 markets we are aiming at ... the first market is people offering rooms to rent who want the highest rental return. The second market is people looking to rent safe, high-quality rooms, in houses that are well managed and looked after.

Industry/Entity Type

Share Economy

Logo Text

LodVenra

Number of Pages Required

5+ page

Font styles to use
Sans Serif

Colors
3276b5

Requirements
Must have
• A messaging system whereby we can create direct communication between those offering rooms and those looking for rooms.
• A call to action that says " Schedule an Inspection"
• Landing page for promoting rooms
• A home page for showing stock.
• Profile page for those selling rooms
• Profile page for those looking for rooms.
• A scheduling calendar for booking inspections
Nice to have
• Pages where new residents can lock in a room.. pay bond and rents.. and sign contracts
• Notifications
• SMS capabilities in the backend.
Should not have
• No script or handwriting fonts.

```html
<!DOCTYPE html>
<html lang="en">
<head>
<meta charset="utf-8">
<title>Lodvenra – High Quality Share Accommodation</title>
<link href="https://fonts.googleapis.com/css2?family=Jost:wght@400;500;600;700&display=swap" rel="stylesheet">
<style>
:root{
  --blue:#3276b5;
  --blue-dark:#28619a;
  --orange:#f7941d;
  --ink:#2b2f36;
  --muted:#8a9099;
  --line:#e2e5ea;
  --soft:#f3f4f7;
  --white:#ffffff;
}
*{box-sizing:border-box;margin:0;padding:0}
html,body{width:1200px;height:2736px;overflow:hidden}
body{font-family:"Jost",Arial,sans-serif;color:var(--ink);background:var(--white);font-size:12px}
.wrap{width:900px;margin:0 auto;position:relative}

/* hero */
.hero{height:390px;position:relative;
  background:linear-gradient(180deg,rgba(30,28,30,.55),rgba(30,28,30,.35)),
  linear-gradient(100deg,#9a6a4e 0%,#c99b7c 35%,#e4d3c2 55%,#b57a5c 80%,#7b4a36 100%);}
.topbar{display:flex;justify-content:space-between;align-items:center;padding-top:22px}
.brand{display:flex;align-items:center;gap:8px;color:var(--white);font-weight:600;font-size:24px;letter-spacing:.2px}
.brand .dot{width:10px;height:10px;border-radius:50%;background:var(--white)}
.top-actions{display:flex;gap:10px}
.top-btn{font-size:9px;font-weight:600;letter-spacing:.6px;padding:7px 14px;border:1px solid var(--white);color:var(--white);text-transform:uppercase}
.top-btn.fill{background:var(--blue);border-color:var(--blue)}
.hero h1{margin-top:92px;text-align:center;color:var(--white);font-size:36px;line-height:1.15;font-weight:700;letter-spacing:1px}
.search{margin:30px auto 0;width:560px;height:40px;display:flex;background:var(--white)}
.search .field{flex:1;display:flex;align-items:center;padding:0 14px;color:var(--muted);font-size:11px;gap:8px}
.search .select{width:150px;border-left:1px solid var(--line);display:flex;align-items:center;justify-content:space-between;padding:0 12px;color:var(--ink);font-size:11px}
.search .go{width:92px;background:var(--orange);color:var(--white);font-weight:600;font-size:11px;display:flex;align-items:center;justify-content:center;gap:6px}

/* rooms */
.rooms{background:var(--soft);height:880px;padding-top:28px}
.cta-row{display:flex;justify-content:center;gap:20px}
.cta{width:150px;height:40px;display:flex;align-items:center;justify-content:center;color:var(--white);font-weight:600;font-size:12px;letter-spacing:.6px}
.cta.orange{background:var(--orange)}
.cta.blue{background:var(--blue)}
.sec-head{display:flex;justify-content:space-between;align-items:center;border-bottom:1px solid var(--line);padding-bottom:10px}
.sec-head h2{font-size:18px;font-weight:600}
.view-all{font-size:9px;font-weight:600;letter-spacing:.6px;border:1px solid #c8ccd3;padding:4px 12px;color:var(--muted)}
.rooms .sec-head{margin-top:44px}
.room-grid{display:grid;grid-template-columns:repeat(4,216px);gap:26px 12px;margin-top:20px}
.room{background:var(--white);height:290px;box-shadow:0 1px 3px rgba(0,0,0,.08)}
.room .photo{height:168px;position:relative}
.tag{position:absolute;left:10px;bottom:-9px;font-size:8px;font-weight:600;letter-spacing:.5px;color:var(--white);padding:4px 10px;background:var(--blue)}
.tag.alt{background:var(--orange)}
.room h3{font-size:13px;font-weight:600;padding:20px 14px 8px}
.facts{display:grid;grid-template-columns:1fr 1fr;gap:6px 8px;padding:0 14px;color:var(--muted);font-size:10px}
.facts span{display:flex;align-items:center;gap:6px}
.facts svg{flex:none}

/* renters */
.renters{height:820px;padding-top:40px}
.renter-grid{display:grid;grid-template-columns:repeat(3,290px);gap:30px 15px;margin-top:22px}
.renter{height:330px;background:var(--white);border:1px solid var(--line);text-align:center}
.renter .photo{height:160px;position:relative}
.renter .tag{left:50%;transform:translateX(-50%);white-space:nowrap}
.renter h3{font-size:13px;font-weight:600;margin-top:24px;letter-spacing:.4px}
.renter .sub{font-size:10px;color:var(--muted);margin-top:3px}
.renter p{font-size:10px;line-height:1.6;color:var(--muted);padding:12px 26px 0}
.renter.featured{background:var(--orange);border-color:var(--orange)}
.renter.featured h3,.renter.featured .sub,.renter.featured p{color:var(--white)}
.renter.featured .tag{background:var(--blue-dark)}

/* testimonials */
.reviews{background:var(--soft);height:330px;padding-top:30px}
.reviews h2{text-align:center;font-size:20px;font-weight:600}
.review-row{display:flex;align-items:center;justify-content:space-between;margin-top:38px}
.arrow{width:22px;height:22px;border-radius:50%;background:#c7cbd2;display:flex;align-items:center;justify-content:center}
.review-list{display:grid;grid-template-columns:repeat(4,196px);gap:18px}
.review{background:var(--white);height:184px;padding:16px;box-shadow:0 1px 3px rgba(0,0,0,.08)}
.review h4{font-size:11px;font-weight:600;color:var(--blue)}
.review p{font-size:9.5px;line-height:1.6;color:var(--muted);margin-top:8px}
.reviewer{display:flex;align-items:center;gap:8px;margin-top:14px}
.avatar{width:28px;height:28px;border-radius:50%;background:linear-gradient(135deg,#c9a58b,#8d6b58)}
.reviewer b{font-size:10px;font-weight:600;display:block}
.stars{display:flex;gap:2px;margin-top:2px}

/* press */
.press{height:110px;display:flex;align-items:center}
.press .wrap{display:flex;align-items:center;justify-content:space-between}
.press-label{font-size:9px;font-weight:600;color:var(--blue);line-height:1.2;letter-spacing:.5px}
.press-name{font-size:14px;font-weight:600;color:#5b6068}

/* footer */
.footer{background:var(--blue);height:206px;color:var(--white);padding-top:34px}
.footer .wrap{display:grid;grid-template-columns:250px 100px 100px 100px 200px;gap:0 36px}
.footer .brand{font-size:22px}
.footer .about{font-size:9.5px;line-height:1.6;opacity:.85;margin-top:10px}
.footer .copy{font-size:8.5px;opacity:.7;margin-top:22px}
.footer ul{list-style:none;font-size:10px;line-height:1.9;opacity:.9}
.sub-form input{display:block;width:100%;height:24px;border:0;margin-bottom:8px;padding:0 8px;font-family:inherit;font-size:9px;color:var(--muted)}
.socials{display:flex;gap:8px;margin-top:6px}
.socials span{width:18px;height:18px;border-radius:50%;background:rgba(255,255,255,.35)}
</style>
</head>
<body>

<header class="hero">
  <div class="wrap">
    <div class="topbar">
      <div class="brand"><span class="dot"></span>lodvenra</div>
      <div class="top-actions">
        <span class="top-btn">List your room free</span>
        <span class="top-btn fill">Log in / Sign up</span>
      </div>
    </div>
    <h1>HIGH QUALITY<br>SHARE ACCOMMODATION</h1>
    <div class="search">
      <div class="field">
        <svg width="12" height="12" viewBox="0 0 12 12"><circle cx="5" cy="5" r="3.8" fill="none" stroke="#8a9099" stroke-width="1.4"/><path d="M8 8l3 3" stroke="#8a9099" stroke-width="1.4"/></svg>
        Search for rooms by suburb or city
      </div>
      <div class="select">I am looking for
        <svg width="8" height="5" viewBox="0 0 8 5"><path d="M0 0l4 5 4-5z" fill="#2b2f36"/></svg>
      </div>
      <div class="go">
        <svg width="11" height="11" viewBox="0 0 12 12"><circle cx="5" cy="5" r="3.8" fill="none" stroke="#fff" stroke-width="1.4"/><path d="M8 8l3 3" stroke="#fff" stroke-width="1.4"/></svg>
        SEARCH
      </div>
    </div>
  </div>
</header>

<section class="rooms">
  <div class="wrap">
    <div class="cta-row">
      <span class="cta orange">LIST MY PLACE</span>
      <span class="cta blue">FIND A PLACE</span>
    </div>
    <div class="sec-head"><h2>Available Rooms</h2><span class="view-all">VIEW ALL</span></div>

    <div class="room-grid">
      <!-- room card -->
      <article class="room">
        <div class="photo" role="img" aria-label="Photo of a bright bedroom with a made double bed" style="background:linear-gradient(135deg,#d9d4cc,#a99a88)"><span class="tag">ENSUITE ROOM</span></div>
        <h3>MARROW POINT, NC</h3>
        <div class="facts">
          <span><svg width="10" height="10" viewBox="0 0 10 10"><rect x="1" y="2" width="8" height="7" fill="none" stroke="#8a9099"/><path d="M1 4h8" stroke="#8a9099"/></svg>12 Jun</span>
          <span><svg width="10" height="10" viewBox="0 0 10 10"><rect x="1" y="3" width="8" height="5" fill="none" stroke="#8a9099"/></svg>$320/wk</span>
          <span><svg width="10" height="10" viewBox="0 0 10 10"><path d="M1 5h8v2H1zM2 7v2M8 7v2" fill="none" stroke="#8a9099"/></svg>2 Baths</span>
          <span><svg width="10" height="10" viewBox="0 0 10 10"><path d="M1 8V3M1 6h8v2M3 5h3" fill="none" stroke="#8a9099"/></svg>3 Beds</span>
          <span><svg width="10" height="10" viewBox="0 0 10 10"><path d="M1 8l4-6 4 6z" fill="none" stroke="#8a9099"/></svg>Furnished</span>
          <span><svg width="10" height="10" viewBox="0 0 10 10"><circle cx="5" cy="5" r="4" fill="none" stroke="#8a9099"/></svg>Parking</span>
        </div>
      </article>
      <article class="room">
        <div class="photo" role="img" aria-label="Photo of a warm bedroom with timber furniture" style="background:linear-gradient(135deg,#c9a987,#7d5b44)"><span class="tag alt">NEW ROOM</span></div>
        <h3>MARROW POINT, NC</h3>
        <div class="facts">
          <span><svg width="10" height="10" viewBox="0 0 10 10"><rect x="1" y="2" width="8" height="7" fill="none" stroke="#8a9099"/><path d="M1 4h8" stroke="#8a9099"/></svg>18 Jun</span>
          <span><svg width="10" height="10" viewBox="0 0 10 10"><rect x="1" y="3" width="8" height="5" fill="none" stroke="#8a9099"/></svg>$290/wk</span>
          <span><svg width="10" height="10" viewBox="0 0 10 10"><path d="M1 5h8v2H1zM2 7v2M8 7v2" fill="none" stroke="#8a9099"/></svg>1 Bath</span>
          <span><svg width="10" height="10" viewBox="0 0 10 10"><path d="M1 8V3M1 6h8v2M3 5h3" fill="none" stroke="#8a9099"/></svg>2 Beds</span>
          <span><svg width="10" height="10" viewBox="0 0 10 10"><path d="M1 8l4-6 4 6z" fill="none" stroke="#8a9099"/></svg>Furnished</span>
          <span><svg width="10" height="10" viewBox="0 0 10 10"><circle cx="5" cy="5" r="4" fill="none" stroke="#8a9099"/></svg>Parking</span>
        </div>
      </article>
      <article class="room">
        <div class="photo" role="img" aria-label="Photo of a modern bedroom with a large window" style="background:linear-gradient(135deg,#e2ddd4,#9b8b79)"><span class="tag">ENSUITE ROOM</span></div>
        <h3>MARROW POINT, NC</h3>
        <div class="facts">
          <span><svg width="10" height="10" viewBox="0 0 10 10"><rect x="1" y="2" width="8" height="7" fill="none" stroke="#8a9099"/><path d="M1 4h8" stroke="#8a9099"/></svg>20 Jun</span>
          <span><svg width="10" height="10" viewBox="0 0 10 10"><rect x="1" y="3" width="8" height="5" fill="none" stroke="#8a9099"/></svg>$340/wk</span>
          <span><svg width="10" height="10" viewBox="0 0 10 10"><path d="M1 5h8v2H1zM2 7v2M8 7v2" fill="none" stroke="#8a9099"/></svg>2 Baths</span>
          <span><svg width="10" height="10" viewBox="0 0 10 10"><path d="M1 8V3M1 6h8v2M3 5h3" fill="none" stroke="#8a9099"/></svg>3 Beds</span>
          <span><svg width="10" height="10" viewBox="0 0 10 10"><path d="M1 8l4-6 4 6z" fill="none" stroke="#8a9099"/></svg>Furnished</span>
          <span><svg width="10" height="10" viewBox="0 0 10 10"><circle cx="5" cy="5" r="4" fill="none" stroke="#8a9099"/></svg>Parking</span>
        </div>
      </article>
      <article class="room">
        <div class="photo" role="img" aria-label="Photo of a cosy bedroom with brick feature wall" style="background:linear-gradient(135deg,#b98b6d,#6e4a39)"><span class="tag alt">NEW ROOM</span></div>
        <h3>MARROW POINT, NC</h3>
        <div class="facts">
          <span><svg width="10" height="10" viewBox="0 0 10 10"><rect x="1" y="2" width="8" height="7" fill="none" stroke="#8a9099"/><path d="M1 4h8" stroke="#8a9099"/></svg>24 Jun</span>
          <span><svg width="10" height="10" viewBox="0 0 10 10"><rect x="1" y="3" width="8" height="5" fill="none" stroke="#8a9099"/></svg>$310/wk</span>
          <span><svg width="10" height="10" viewBox="0 0 10 10"><path d="M1 5h8v2H1zM2 7v2M8 7v2" fill="none" stroke="#8a9099"/></svg>2 Baths</span>
          <span><svg width="10" height="10" viewBox="0 0 10 10"><path d="M1 8V3M1 6h8v2M3 5h3" fill="none" stroke="#8a9099"/></svg>4 Beds</span>
          <span><svg width="10" height="10" viewBox="0 0 10 10"><path d="M1 8l4-6 4 6z" fill="none" stroke="#8a9099"/></svg>Furnished</span>
          <span><svg width="10" height="10" viewBox="0 0 10 10"><circle cx="5" cy="5" r="4" fill="none" stroke="#8a9099"/></svg>Parking</span>
        </div>
      </article>
      <article class="room">
        <div class="photo" role="img" aria-label="Photo of a bedroom with white linen and lamps" style="background:linear-gradient(135deg,#ddd6cd,#8f7e6d)"><span class="tag alt">NEW ROOM</span></div>
        <h3>MARROW POINT, NC</h3>
        <div class="facts">
          <span><svg width="10" height="10" viewBox="0 0 10 10"><rect x="1" y="2" width="8" height="7" fill="none" stroke="#8a9099"/><path d="M1 4h8" stroke="#8a9099"/></svg>02 Jul</span>
          <span><svg width="10" height="10" viewBox="0 0 10 10"><rect x="1" y="3" width="8" height="5" fill="none" stroke="#8a9099"/></svg>$300/wk</span>
          <span><svg width="10" height="10" viewBox="0 0 10 10"><path d="M1 5h8v2H1zM2 7v2M8 7v2" fill="none" stroke="#8a9099"/></svg>1 Bath</span>
          <span><svg width="10" height="10" viewBox="0 0 10 10"><path d="M1 8V3M1 6h8v2M3 5h3" fill="none" stroke="#8a9099"/></svg>2 Beds</span>
          <span><svg width="10" height="10" viewBox="0 0 10 10"><path d="M1 8l4-6 4 6z" fill="none" stroke="#8a9099"/></svg>Furnished</span>
          <span><svg width="10" height="10" viewBox="0 0 10 10"><circle cx="5" cy="5" r="4" fill="none" stroke="#8a9099"/></svg>Parking</span>
        </div>
      </article>
      <article class="room">
        <div class="photo" role="img" aria-label="Photo of a spacious master bedroom" style="background:linear-gradient(135deg,#cbbfb2,#76635a)"><span class="tag">ENSUITE ROOM</span></div>
        <h3>MARROW POINT, NC</h3>
        <div class="facts">
          <span><svg width="10" height="10" viewBox="0 0 10 10"><rect x="1" y="2" width="8" height="7" fill="none" stroke="#8a9099"/><path d="M1 4h8" stroke="#8a9099"/></svg>05 Jul</span>
          <span><svg width="10" height="10" viewBox="0 0 10 10"><rect x="1" y="3" width="8" height="5" fill="none" stroke="#8a9099"/></svg>$360/wk</span>
          <span><svg width="10" height="10" viewBox="0 0 10 10"><path d="M1 5h8v2H1zM2 7v2M8 7v2" fill="none" stroke="#8a9099"/></svg>2 Baths</span>
          <span><svg width="10" height="10" viewBox="0 0 10 10"><path d="M1 8V3M1 6h8v2M3 5h3" fill="none" stroke="#8a9099"/></svg>3 Beds</span>
          <span><svg width="10" height="10" viewBox="0 0 10 10"><path d="M1 8l4-6 4 6z" fill="none" stroke="#8a9099"/></svg>Furnished</span>
          <span><svg width="10" height="10" viewBox="0 0 10 10"><circle cx="5" cy="5" r="4" fill="none" stroke="#8a9099"/></svg>Parking</span>
        </div>
      </article>
      <article class="room">
        <div class="photo" role="img" aria-label="Photo of a bedroom with dark timber bedhead" style="background:linear-gradient(135deg,#bfa48c,#5f4536)"><span class="tag alt">NEW ROOM</span></div>
        <h3>MARROW POINT, NC</h3>
        <div class="facts">
          <span><svg width="10" height="10" viewBox="0 0 10 10"><rect x="1" y="2" width="8" height="7" fill="none" stroke="#8a9099"/><path d="M1 4h8" stroke="#8a9099"/></svg>09 Jul</span>
          <span><svg width="10" height="10" viewBox="0 0 10 10"><rect x="1" y="3" width="8" height="5" fill="none" stroke="#8a9099"/></svg>$280/wk</span>
          <span><svg width="10" height="10" viewBox="0 0 10 10"><path d="M1 5h8v2H1zM2 7v2M8 7v2" fill="none" stroke="#8a9099"/></svg>1 Bath</span>
          <span><svg width="10" height="10" viewBox="0 0 10 10"><path d="M1 8V3M1 6h8v2M3 5h3" fill="none" stroke="#8a9099"/></svg>2 Beds</span>
          <span><svg width="10" height="10" viewBox="0 0 10 10"><path d="M1 8l4-6 4 6z" fill="none" stroke="#8a9099"/></svg>Furnished</span>
          <span><svg width="10" height="10" viewBox="0 0 10 10"><circle cx="5" cy="5" r="4" fill="none" stroke="#8a9099"/></svg>Parking</span>
        </div>
      </article>
      <article class="room">
        <div class="photo" role="img" aria-label="Photo of a light bedroom with a reading chair" style="background:linear-gradient(135deg,#e0d8cd,#a48f7b)"><span class="tag">ENSUITE ROOM</span></div>
        <h3>MARROW POINT, NC</h3>
        <div class="facts">
          <span><svg width="10" height="10" viewBox="0 0 10 10"><rect x="1" y="2" width="8" height="7" fill="none" stroke="#8a9099"/><path d="M1 4h8" stroke="#8a9099"/></svg>14 Jul</span>
          <span><svg width="10" height="10" viewBox="0 0 10 10"><rect x="1" y="3" width="8" height="5" fill="none" stroke="#8a9099"/></svg>$330/wk</span>
          <span><svg width="10" height="10" viewBox="0 0 10 10"><path d="M1 5h8v2H1zM2 7v2M8 7v2" fill="none" stroke="#8a9099"/></svg>2 Baths</span>
          <span><svg width="10" height="10" viewBox="0 0 10 10"><path d="M1 8V3M1 6h8v2M3 5h3" fill="none" stroke="#8a9099"/></svg>3 Beds</span>
          <span><svg width="10" height="10" viewBox="0 0 10 10"><path d="M1 8l4-6 4 6z" fill="none" stroke="#8a9099"/></svg>Furnished</span>
          <span><svg width="10" height="10" viewBox="0 0 10 10"><circle cx="5" cy="5" r="4" fill="none" stroke="#8a9099"/></svg>Parking</span>
        </div>
      </article>
    </div>
  </div>
</section>

<section class="renters">
  <div class="wrap">
    <div class="sec-head"><h2>Know Your Renters</h2><span class="view-all">VIEW ALL</span></div>
    <div class="renter-grid">
      <article class="renter">
        <div class="photo" role="img" aria-label="Portrait photo of renter Tessa Marlow" style="background:linear-gradient(135deg,#d8c6b4,#8f7462)"><span class="tag">BUDGET $250/WK</span></div>
        <h3>TESSA MARLOW</h3><div class="sub">Looking in Sydney</div>
        <p>Quiet professional who works long hours, keeps shared spaces tidy and is looking for a calm, well managed home.</p>
      </article>
      <article class="renter featured">
        <div class="photo" role="img" aria-label="Portrait photo of renter Davin Oakhurst" style="background:linear-gradient(135deg,#c9b3a0,#6f5646)"><span class="tag">BUDGET $300/WK</span></div>
        <h3>DAVIN OAKHURST</h3><div class="sub">Looking in Sydney</div>
        <p>Friendly engineer relocating for work, non smoker, enjoys cooking and wants a safe share house close to transport.</p>
      </article>
      <article class="renter">
        <div class="photo" role="img" aria-label="Portrait photo of renter Lena Carrow" style="background:linear-gradient(135deg,#e0cfbf,#9a7d69)"><span class="tag">BUDGET $280/WK</span></div>
        <h3>LENA CARROW</h3><div class="sub">Looking in Sydney</div>
        <p>Postgraduate student who values a clean, quiet study space and respectful housemates in an executive style home.</p>
      </article>
      <article class="renter">
        <div class="photo" role="img" aria-label="Portrait photo of renter Davin Oakhurst" style="background:linear-gradient(135deg,#bfa997,#5e4a3e)"><span class="tag">BUDGET $260/WK</span></div>
        <h3>DAVIN OAKHURST</h3><div class="sub">Looking in Sydney</div>
        <p>Easygoing designer working from home, tidy and organised, looking for a bright room in a welcoming share house.</p>
      </article>
      <article class="renter">
        <div class="photo" role="img" aria-label="Portrait photo of renter Davin Oakhurst" style="background:linear-gradient(135deg,#d2bfae,#7e6352)"><span class="tag">BUDGET $320/WK</span></div>
        <h3>DAVIN OAKHURST</h3><div class="sub">Looking in Sydney</div>
        <p>Nurse on rotating shifts, considerate and reliable, seeking a secure room with ensuite in a well kept house.</p>
      </article>
      <article class="renter">
        <div class="photo" role="img" aria-label="Portrait photo of renter Lena Carrow" style="background:linear-gradient(135deg,#cdb8a6,#735b4b)"><span class="tag">BUDGET $290/WK</span></div>
        <h3>LENA CARROW</h3><div class="sub">Looking in Sydney</div>
        <p>Marketing manager new to the city, loves weekend walks and wants a furnished room in a friendly, managed home.</p>
      </article>
    </div>
  </div>
</section>

<section class="reviews">
  <div class="wrap">
    <h2>What customers are saying...</h2>
    <div class="review-row">
      <span class="arrow"><svg width="8" height="8" viewBox="0 0 8 8"><path d="M5.5 1L2.5 4l3 3" fill="none" stroke="#fff" stroke-width="1.5"/></svg></span>
      <div class="review-list">
        <div class="review"><h4>Amazing!!</h4><p>Found a beautiful room within a week. The inspection booking was simple and the house is spotless and well run.</p>
          <div class="reviewer"><span class="avatar" role="img" aria-label="Reviewer avatar"></span><div><b>Mia Corran</b><div class="stars"><svg width="50" height="9" viewBox="0 0 50 9"><g fill="#f7941d"><path d="M4.5 0l1.4 3 3.1.3-2.4 2 .8 3.2-2.9-1.7-2.9 1.7.8-3.2L0 3.3 3.1 3z"/><path transform="translate(10)" d="M4.5 0l1.4 3 3.1.3-2.4 2 .8 3.2-2.9-1.7-2.9 1.7.8-3.2L0 3.3 3.1 3z"/><path transform="translate(20)" d="M4.5 0l1.4 3 3.1.3-2.4 2 .8 3.2-2.9-1.7-2.9 1.7.8-3.2L0 3.3 3.1 3z"/><path transform="translate(30)" d="M4.5 0l1.4 3 3.1.3-2.4 2 .8 3.2-2.9-1.7-2.9 1.7.8-3.2L0 3.3 3.1 3z"/><path transform="translate(40)" d="M4.5 0l1.4 3 3.1.3-2.4 2 .8 3.2-2.9-1.7-2.9 1.7.8-3.2L0 3.3 3.1 3z"/></g></svg></div></div></div></div>
        <div class="review"><h4>Amazing!!</h4><p>My rooms are always full now and the rental return is higher than before. Great support from the team.</p>
          <div class="reviewer"><span class="avatar" role="img" aria-label="Reviewer avatar"></span><div><b>Owen Talbry</b><div class="stars"><svg width="50" height="9" viewBox="0 0 50 9"><g fill="#f7941d"><path d="M4.5 0l1.4 3 3.1.3-2.4 2 .8 3.2-2.9-1.7-2.9 1.7.8-3.2L0 3.3 3.1 3z"/><path transform="translate(10)" d="M4.5 0l1.4 3 3.1.3-2.4 2 .8 3.2-2.9-1.7-2.9 1.7.8-3.2L0 3.3 3.1 3z"/><path transform="translate(20)" d="M4.5 0l1.4 3 3.1.3-2.4 2 .8 3.2-2.9-1.7-2.9 1.7.8-3.2L0 3.3 3.1 3z"/><path transform="translate(30)" d="M4.5 0l1.4 3 3.1.3-2.4 2 .8 3.2-2.9-1.7-2.9 1.7.8-3.2L0 3.3 3.1 3z"/><path transform="translate(40)" d="M4.5 0l1.4 3 3.1.3-2.4 2 .8 3.2-2.9-1.7-2.9 1.7.8-3.2L0 3.3 3.1 3z"/></g></svg></div></div></div></div>
        <div class="review"><h4>Amazing!!</h4><p>Messaging the owner directly made everything easy. I felt safe moving in and the housemates are lovely.</p>
          <div class="reviewer"><span class="avatar" role="img" aria-label="Reviewer avatar"></span><div><b>Priya Lenn</b><div class="stars"><svg width="50" height="9" viewBox="0 0 50 9"><g fill="#f7941d"><path d="M4.5 0l1.4 3 3.1.3-2.4 2 .8 3.2-2.9-1.7-2.9 1.7.8-3.2L0 3.3 3.1 3z"/><path transform="translate(10)" d="M4.5 0l1.4 3 3.1.3-2.4 2 .8 3.2-2.9-1.7-2.9 1.7.8-3.2L0 3.3 3.1 3z"/><path transform="translate(20)" d="M4.5 0l1.4 3 3.1.3-2.4 2 .8 3.2-2.9-1.7-2.9 1.7.8-3.2L0 3.3 3.1 3z"/><path transform="translate(30)" d="M4.5 0l1.4 3 3.1.3-2.4 2 .8 3.2-2.9-1.7-2.9 1.7.8-3.2L0 3.3 3.1 3z"/><path transform="translate(40)" d="M4.5 0l1.4 3 3.1.3-2.4 2 .8 3.2-2.9-1.7-2.9 1.7.8-3.2L0 3.3 3.1 3z"/></g></svg></div></div></div></div>
        <div class="review"><h4>Amazing!!</h4><p>High quality rooms and a clear process from inspection to signing. I would recommend it to any renter.</p>
          <div class="reviewer"><span class="avatar" role="img" aria-label="Reviewer avatar"></span><div><b>Jonah Vell</b><div class="stars"><svg width="50" height="9" viewBox="0 0 50 9"><g fill="#f7941d"><path d="M4.5 0l1.4 3 3.1.3-2.4 2 .8 3.2-2.9-1.7-2.9 1.7.8-3.2L0 3.3 3.1 3z"/><path transform="translate(10)" d="M4.5 0l1.4 3 3.1.3-2.4 2 .8 3.2-2.9-1.7-2.9 1.7.8-3.2L0 3.3 3.1 3z"/><path transform="translate(20)" d="M4.5 0l1.4 3 3.1.3-2.4 2 .8 3.2-2.9-1.7-2.9 1.7.8-3.2L0 3.3 3.1 3z"/><path transform="translate(30)" d="M4.5 0l1.4 3 3.1.3-2.4 2 .8 3.2-2.9-1.7-2.9 1.7.8-3.2L0 3.3 3.1 3z"/><path transform="translate(40)" d="M4.5 0l1.4 3 3.1.3-2.4 2 .8 3.2-2.9-1.7-2.9 1.7.8-3.2L0 3.3 3.1 3z"/></g></svg></div></div></div></div>
      </div>
      <span class="arrow"><svg width="8" height="8" viewBox="0 0 8 8"><path d="M2.5 1l3 3-3 3" fill="none" stroke="#fff" stroke-width="1.5"/></svg></span>
    </div>
  </div>
</section>

<section class="press">
  <div class="wrap">
    <div class="press-label">AS SEEN<br>IN THE PRESS</div>
    <span class="press-name">Daily Ledger</span>
    <span class="press-name">Estate Wire</span>
    <span class="press-name">Coastal Herald</span>
    <span class="press-name">Stackline</span>
    <span class="press-name">Harbor Post</span>
  </div>
</section>

<footer class="footer">
  <div class="wrap">
    <div>
      <div class="brand"><span class="dot"></span>lodvenra</div>
      <p class="about">Executive share accommodation connecting people who offer quality rooms with renters looking for safe, well managed homes.</p>
      <p class="copy">Copyright © 2024 Lodvenra. All rights reserved.</p>
    </div>
    <ul><li>Find a Room</li><li>List a Room</li><li>How it Works</li><li>Pricing</li></ul>
    <ul><li>About Us</li><li>Our Team</li><li>Careers</li><li>Contact</li></ul>
    <ul><li>Help Centre</li><li>Safety</li><li>Terms</li><li>Privacy</li></ul>
    <div class="sub-form">
      <input type="text" value="Your email address" aria-label="Email">
      <input type="text" value="Your suburb" aria-label="Suburb">
      <div class="socials"><span></span><span></span><span></span><span></span></div>
    </div>
  </div>
</footer>

</body>
</html>
```